Tri-fold Brochure design for Bed & Breakfast

I would like a trifold Brochure for my Bed & Breakfast, The Lodge at Birchwater Cove in Holderness, NH. I would like to put as many photos as possible without looking too busy and have space for me to add verbiage about the amenities we offer. We are family and dog friendly and would like to highlight that unique quality. I would like to showcase the rooms, breakfast, family and dog specific amenities, outdoor areas and the beach. Our website is www.lodgeatbirchwatercove.example

Target Market(s)

Families and people with Dogs

Industry/Entity Type

Hospitality

Font styles to use
Serif

Colors
0054AA
0677BA
7BADD7
CADEEF
E8F1F8

Requirements
Must have
• Our logo, space for multiple photos, appropriate for a Bed & Breakfast

```html
<!DOCTYPE html>
<html lang="en">
<head>
<meta charset="utf-8">
<title>The Lodge at Birchwater Cove – Tri-fold Brochure</title>
<link rel="stylesheet" href="https://fonts.googleapis.com/css2?family=Libre+Baskerville:ital,wght@0,400;0,700;1,400&family=Poppins:ital,wght@0,400;0,600;0,700;1,400;1,600&display=swap">
<style>
:root{
  --navy:#0054AA;
  --blue:#0677BA;
  --sky:#7BADD7;
  --mist:#CADEEF;
  --ice:#E8F1F8;
  --white:#ffffff;
  --ink:#1d2533;
  --serif:"Libre Baskerville", Georgia, serif;
  --sans:"Poppins", Arial, sans-serif;
}
*{box-sizing:border-box;margin:0;padding:0}
html,body{width:803px;height:1200px;overflow:hidden;background:#d9d9d9;font-family:var(--sans);color:var(--ink)}
.canvas{position:relative;width:803px;height:1200px}
.spread{position:absolute;left:11px;width:780px;height:540px;background:var(--white);overflow:hidden;box-shadow:0 4px 14px rgba(0,0,0,.25)}
.spread--outside{top:40px}
.spread--inside{top:620px}
.abs{position:absolute}
.photo{position:absolute}
.shapes{position:absolute;left:0;top:0}

/* outside – intro panel */
.intro{left:14px;top:14px;width:232px;font-size:6.6px;line-height:1.35}
.intro p{margin-bottom:9px}
.intro b{font-weight:700}
.intro-photo{top:262px;width:104px;height:112px;border:3px solid var(--white);border-radius:6px}
.reviews{left:14px;top:392px;width:232px;height:112px;border:1px solid var(--white);border-radius:8px;padding:8px 12px;color:var(--white)}
.reviews h3{font-family:var(--serif);font-weight:700;font-size:17px;margin:-18px 0 6px 18px;background:var(--navy);display:inline-block;padding:0 6px}
.reviews p{font-style:italic;font-size:6px;line-height:1.45}
.reviews .sign{display:flex;justify-content:space-between;margin-top:6px;font-style:italic;font-weight:600;font-size:7px}
.stars{letter-spacing:2px;font-size:10px;font-style:normal}

/* outside – contact panel */
.contact{left:272px;top:16px;width:240px;color:var(--white)}
.contact .row{display:flex;align-items:center;gap:6px}
.contact .phone{font-family:var(--serif);font-size:21px}
.contact .small{font-family:var(--serif);font-size:6.6px;line-height:1.3;margin-top:6px}

/* outside – cover panel */
.brand{display:flex;align-items:center;justify-content:center;text-align:center;font-family:var(--serif);font-weight:700;font-size:16px;line-height:1.2;color:var(--ink)}
.welcome{left:520px;top:362px;width:260px;text-align:center}
.welcome .pre{font-size:10px;letter-spacing:.5px}
.welcome h1{font-family:var(--serif);font-weight:700;font-size:20px;line-height:1.05;color:var(--navy);margin:3px 0 8px}
.welcome .tag{font-size:8px;line-height:1.35}
.welcome .tag b{font-weight:700}
.webbar{left:520px;top:500px;width:260px;height:40px;background:var(--sky);color:var(--white);font-weight:600;font-size:8.5px;display:flex;align-items:center;justify-content:center}

/* inside */
.strip-title{left:-185px;top:258px;width:410px;transform:rotate(-90deg);color:var(--white);font-family:var(--serif);font-weight:700;font-size:14px;white-space:nowrap;text-align:center}
.feature{position:absolute;width:180px;text-align:center}
.feature .pic{height:92px;border-radius:9px;border:2px solid var(--mist)}
.feature h4{font-family:var(--serif);font-weight:700;font-size:7.8px;color:var(--navy);margin-top:5px}
.feature p{font-size:6.4px;line-height:1.35;margin-top:2px}
.rooms{left:540px;top:332px;width:226px;color:var(--white)}
.rooms h2{font-family:var(--serif);font-weight:700;font-size:17px;line-height:1.05;text-align:right}
.rooms .motto{font-size:6.8px;text-align:right;margin-top:4px}
.rooms .rule{height:1px;background:var(--mist);margin:10px 0 10px 20px}
.rooms p{font-size:6.4px;line-height:1.4;margin-bottom:9px}
.rooms b{font-weight:700}
.brand--inside{left:540px;top:10px;width:220px;height:110px}
</style>
</head>
<body>
<main class="canvas">

  <!-- OUTSIDE SPREAD -->
  <section class="spread spread--outside" aria-label="Brochure outside">
    <svg class="shapes" width="780" height="540" viewBox="0 0 780 540" aria-hidden="true">
      <polygon points="0,250 140,236 260,250 260,540 0,540" fill="var(--navy)"/>
      <polygon points="0,236 120,222 260,236 260,250 140,236 0,250" fill="var(--sky)"/>
      <rect x="0" y="520" width="260" height="20" fill="var(--sky)"/>
      <rect x="260" y="0" width="260" height="540" fill="var(--navy)"/>
      <polygon points="520,280 650,328 780,280 780,300 650,348 520,300" fill="var(--blue)"/>
      <polygon points="520,300 650,348 780,300 780,312 650,360 520,312" fill="var(--navy)"/>
      <polygon points="520,312 650,360 780,312 780,320 650,368 520,320" fill="var(--mist)"/>
    </svg>

    <div class="abs intro">
      <p>We are a <b>high-end, upscale</b> B&amp;B that offers complimentary <b>family &amp; dog friendly amenities &amp; activities</b> to ensure guests and their families have a <b>stress free, fun-filled</b> and <b>memorable vacation experience together.</b></p>
      <p>Having 3 young children and 2 rescue pups, we understand the challenges of finding <b>family-oriented, pet friendly lodging</b> with <b>upscale amenities.</b></p>
      <p>Between the <b>beautiful historic Inn</b> with <b>rustic chic decor</b> and <b>modern amenities,</b> expansive grounds, <b>family fun activities,</b> a menagerie of <b>farm animals</b> and access to <b>beautiful Squam Lake,</b> there truly is something for everyone to enjoy!!</p>
    </div>

    <div class="photo intro-photo" style="left:22px;background:linear-gradient(160deg,#3f6e3a,#8aa67a 55%,#c9c6bd)" role="img" aria-label="Photo of the patio with white Adirondack chairs and a stone fire pit"></div>
    <div class="photo intro-photo" style="left:134px;background:linear-gradient(160deg,#b9794a,#e7cfae 55%,#7a5134)" role="img" aria-label="Photo of the wood-beamed breakfast dining room"></div>

    <div class="abs reviews">
      <h3>Reviews</h3>
      <p>Perfect New England Fall Experience. Clara and her husband were excellent hosts. The breakfast included farm fresh eggs from their own chickens who free roamed the property. Rooms are newly renovated with luxury linens and are very comfortable. The location on the pond is a perfect base camp to explore the surrounding state parks and long fall foliage drives.</p>
      <div class="sign"><span>– Margaret Ellison</span><span class="stars">★★★★★</span></div>
    </div>

    <div class="abs contact">
      <div class="row">
        <svg width="14" height="14" viewBox="0 0 14 14" aria-hidden="true"><circle cx="7" cy="7" r="7" fill="var(--white)"/><path d="M4.5 3.5l1.6 0.2 0.6 1.8-1 .8a5 5 0 0 0 2.2 2.2l.8-1 1.8.6.2 1.6c-.6.6-1.6.8-2.6.3A8 8 0 0 1 4.2 6.1c-.5-1-.3-2 .3-2.6z" fill="var(--navy)"/></svg>
        <span class="phone">555.012.4410</span>
      </div>
      <div class="row small">
        <svg width="12" height="12" viewBox="0 0 12 12" aria-hidden="true"><circle cx="6" cy="6" r="6" fill="var(--white)"/><rect x="3" y="4" width="6" height="4.2" fill="none" stroke="var(--navy)" stroke-width=".8"/><path d="M3 4l3 2.3L9 4" fill="none" stroke="var(--navy)" stroke-width=".8"/></svg>
        <span>innkeepers@lodgeatbirchwatercove.example</span>
      </div>
      <div class="row small" style="margin-top:10px">
        <svg width="12" height="14" viewBox="0 0 12 14" aria-hidden="true"><path d="M6 0a5 5 0 0 1 5 5c0 3.5-5 9-5 9S1 8.5 1 5a5 5 0 0 1 5-5z" fill="var(--white)"/><circle cx="6" cy="5" r="1.8" fill="var(--navy)"/></svg>
        <span>42 Lakeview Road, Holderness,<br>New Hampshire</span>
      </div>
    </div>

    <svg class="shapes" width="780" height="540" viewBox="0 0 780 540" role="img" aria-label="Photo of the stone patio fire pit with Adirondack chairs and woven poufs under tall pines">
      <defs>
        <linearGradient id="patio" x1="0" y1="0" x2="0" y2="1">
          <stop offset="0" stop-color="#3a6a35"/><stop offset=".5" stop-color="#7b9a6c"/><stop offset="1" stop-color="#aaa49a"/>
        </linearGradient>
      </defs>
      <polygon points="260,150 520,150 520,320 440,290 440,540 260,540" fill="url(#patio)"/>
    </svg>

    <div class="photo" style="left:316px;top:128px;width:150px;height:150px;border-radius:50%;border:4px solid var(--white);background:linear-gradient(150deg,#e9edf2,#b8c3cf 60%,#8e99a6)" role="img" aria-label="Photo of a bright guest room with a striped bed"></div>

    <svg class="shapes" width="780" height="540" viewBox="0 0 780 540" role="img" aria-label="Photo of the white farmhouse inn in winter snow with trees">
      <defs>
        <linearGradient id="snow" x1="0" y1="0" x2="0" y2="1">
          <stop offset="0" stop-color="#6f8fb2"/><stop offset=".45" stop-color="#d9e3ec"/><stop offset="1" stop-color="#f2f5f8"/>
        </linearGradient>
      </defs>
      <polygon points="520,0 780,0 780,280 650,328 520,280" fill="url(#snow)"/>
    </svg>
    <svg class="shapes" width="780" height="540" viewBox="0 0 780 540" aria-hidden="true">
      <path d="M600,0 H780 V130 H640 Q600,130 600,90 Z" fill="var(--white)"/>
    </svg>
    <div class="abs brand" style="left:600px;top:0;width:180px;height:130px">The Lodge at<br>Birchwater Cove</div>

    <div class="abs welcome">
      <div class="pre">WELCOME TO</div>
      <h1>THE LODGE AT<br>BIRCHWATER COVE</h1>
      <div class="tag">A top-rated<br><b>FAMILY &amp; DOG FRIENDLY</b><br>Bed &amp; Breakfast near <b>Squam Lake</b><br>in Holderness, <b>New Hampshire</b></div>
    </div>
    <div class="abs webbar">www.lodgeatbirchwatercove.example</div>
  </section>

  <!-- INSIDE SPREAD -->
  <section class="spread spread--inside" aria-label="Brochure inside">
    <svg class="shapes" width="780" height="540" viewBox="0 0 780 540" aria-hidden="true">
      <rect x="0" y="0" width="40" height="540" fill="var(--navy)"/>
      <rect x="30" y="0" width="3" height="540" fill="var(--white)"/>
      <polygon points="520,300 780,220 780,540 520,540" fill="var(--navy)"/>
      <polygon points="520,284 780,204 780,220 520,300" fill="var(--mist)"/>
    </svg>
    <svg class="shapes" width="780" height="540" viewBox="0 0 780 540" role="img" aria-label="Photo of a bedside table with flowers, orange juice and a coffee mug in a white guest room">
      <defs>
        <linearGradient id="bedside" x1="0" y1="0" x2="1" y2="1">
          <stop offset="0" stop-color="#f4f3f1"/><stop offset=".6" stop-color="#dfd6c9"/><stop offset="1" stop-color="#c9b28f"/>
        </linearGradient>
      </defs>
      <polygon points="520,0 780,0 780,204 520,284" fill="url(#bedside)"/>
    </svg>
    <div class="abs brand brand--inside">The Lodge at<br>Birchwater Cove</div>

    <div class="abs strip-title">THE BED &amp; BREAKFAST REIMAGINED</div>

    <div class="feature" style="left:55px;top:12px">
      <div class="pic" style="background:linear-gradient(160deg,#e8e9ea,#8fa2b8 60%,#3f5f8a)" role="img" aria-label="Photo of a bright sitting room with a blue sofa"></div>
      <h4>SPACIOUS ROOMS</h4>
      <p>Well-appointed accommodations with full private bath, A/C, luxury linens, Wi-Fi, Smart TV, Brewmaster RESERVE NOW</p>
    </div>
    <div class="feature" style="left:55px;top:190px">
      <div class="pic" style="background:linear-gradient(160deg,#f1d28a,#d9a55c 50%,#9c2f3a)" role="img" aria-label="Photo of a breakfast plate with fresh berries and orange juice"></div>
      <h4>DELICIOUS BREAKFAST</h4>
      <p>Delicious cooked to order breakfast daily. Made with eggs from the coop and pork from our pigs. Breakfast in bed is always an option!</p>
    </div>
    <div class="feature" style="left:55px;top:368px">
      <div class="pic" style="background:linear-gradient(180deg,#9bb86a,#3d6e8e 45%,#1f4e78)" role="img" aria-label="Photo of guests kayaking on the lake"></div>
      <h4>LAKE ACCESS</h4>
      <p>Complimentary kayaking, stand up paddle boarding &amp; swimming at a private beach just a short walk away. Beach towels &amp; all equipment provided.</p>
    </div>

    <div class="feature" style="left:290px;top:12px">
      <div class="pic" style="background:linear-gradient(90deg,#8a6a4e,#cbb9a2 45%,#f3f3f3 55%,#ffffff)" role="img" aria-label="Photo of a dog resting on a plaid bed beside a social post"></div>
      <h4>DOG WELCOME</h4>
      <p>1/4 acre fully enclosed dog park, dog friendly hiking trails and a special doggie breakfast menu!</p>
    </div>
    <div class="feature" style="left:290px;top:190px">
      <div class="pic" style="background:linear-gradient(160deg,#8aa07a,#c7b9a4 50%,#e0782f)" role="img" aria-label="Photo of children playing around a patio fire pit"></div>
      <h4>FAMILY ENTERTAINMENT</h4>
      <p>Complimentary s'mores, arts &amp; crafts and Parent Date Night- the kids eat pizza &amp; watch a movie with us while you enjoy alone time together!</p>
    </div>
    <div class="feature" style="left:290px;top:368px">
      <div class="pic" style="background:linear-gradient(160deg,#5f8c3e,#a8b58a 50%,#d8cbb6)" role="img" aria-label="Photo of a family relaxing on the lawn"></div>
      <h4>OUTDOOR FUN</h4>
      <p>7+ acres of beautiful grounds, patio with 2 fire pits, farm animals, outdoor play set &amp; sandbox, on-site &amp; nearby hiking trails with amazing lake views.</p>
    </div>

    <div class="abs rooms">
      <h2>ROOMS<br>&amp; SUITES</h2>
      <div class="motto">Eat. Play. Unwind. Repeat</div>
      <div class="rule"></div>
      <p>Our <b>newly renovated</b> accommodations have been completely <b>updated and refurbished</b> with the <b>modern and upscale amenities</b> you deserve. Each of the 9 guest rooms and suites are equipped with <b>5-star luxury linens,</b> spa like bath towels and accessories, personally controlled thermostat &amp; air conditioning, flat screen smart TV's, personal Brewmaster machines with a fine selection of coffees and updated rustic chic decor.</p>
      <p>Savor a delicious <b>cooked to order</b> breakfast daily with fresh eggs from our resident chickens. <b>Breakfast in bed</b> is always an option! Place your order through the smart TV &amp; have breakfast delivered to your room!</p>
    </div>
  </section>

</main>
</body>
</html>
```